R7M Meridian Business Card Design

We need a business card created for our New Business "R7M Meridian"<br/><br/>The business card design is up to you however the following information must be on the business card:<br/><br/>Front of the business card -<br/>Email :dorianv@r7mmeridian.nz<br/>Mobile: +64 (0) 22 4871 659<br/>Website: www.r7mmeridian.nz<br/>Card Owner Name: Dorian Valcourt<br/>Company Title: Business Development Manager<br/>Slogan: "The BEST of both worlds". <br/>Logo On the front attached to the design brief<br/><br/>On the back: <br/>Space on the back for 4 more versions of the logo across the bottom of the card indicating different subsidiary brands - R7M Coffee, R7M Arts, R7M ?? (The card will be used for all of these brands - We Will add the extra subsidiary logos to the design once the design is finished (We are a graphics design team). <br/><br/>Other than that we want a premium feeling logo that remains universally usable depending on the business entity that we are using the card for. The use of bright bold colours would be great but we still want the card to feel premium.
Target Market(s)
Gift Design and Manufacturing Companies
Contact Information for Business Card
Front of the business card -
Email :dorianv@r7mmeridian.nz
Mobile: +64 (0) 22 4871 659
Website: www.r7mmeridian.nz
Card Owner Name: Dorian Valcourt
Company Title: Business Development Manager
Slogan: "The BEST of both worlds".
Logo On the front attached to the design brief

```html
<!DOCTYPE html>
<html lang="en">
<head>
<meta charset="utf-8">
<title>R7M Meridian Business Card</title>
<link href="https://fonts.googleapis.com/css2?family=Nunito:wght@700&family=Open+Sans:wght@400&family=Raleway:wght@400;600&display=swap" rel="stylesheet">
<style>
  :root {
    --page-bg: #c0c0c0;
    --card-white: #ffffff;
    --brand-blue: #36479e;
    --brand-lavender: #8e90d2;
    --frame-grey: #7a7a7a;
    --ink: #111111;
  }
  * { margin: 0; padding: 0; box-sizing: border-box; }
  html, body { width: 960px; height: 1200px; overflow: hidden; }
  body { background: var(--page-bg); position: relative; font-family: "Open Sans", sans-serif; }

  .card {
    position: absolute;
    top: 318px;
    width: 290px;
    height: 508px;
    border-radius: 14px;
    overflow: hidden;
  }
  .card-front { left: 160px; background: var(--card-white); }
  .card-back { left: 506px; background: var(--brand-blue); }

  .card-frame {
    position: absolute;
    inset: 11px;
    border-radius: 16px;
    border: 2px solid var(--frame-grey);
  }
  .card-back .card-frame { border-color: var(--card-white); }

  .brand-mark {
    position: absolute;
    left: 0; right: 0;
    display: flex;
    align-items: center;
    justify-content: center;
    gap: 8px;
    font-family: "Raleway", sans-serif;
    font-weight: 600;
    white-space: nowrap;
  }
  .brand-mark .dot { border-radius: 50%; flex: none; }
  .card-front .brand-mark { top: 128px; font-size: 24px; color: var(--brand-blue); }
  .card-front .brand-mark .dot { width: 16px; height: 16px; border: 3px solid var(--brand-blue); }
  .card-back .brand-mark { top: 184px; font-size: 30px; color: var(--brand-lavender); }
  .card-back .brand-mark .dot { width: 20px; height: 20px; border: 4px solid var(--brand-lavender); }

  .holder-name {
    position: absolute; left: 0; right: 0; top: 236px; text-align: center;
    font-family: "Nunito", sans-serif; font-weight: 700; font-size: 19px; color: var(--ink);
  }
  .holder-role {
    position: absolute; left: 0; right: 0; top: 259px; text-align: center;
    font-family: "Raleway", sans-serif; font-size: 15px; color: var(--brand-blue);
  }

  .contact-list { position: absolute; left: 70px; top: 311px; list-style: none; }
  .contact-list li {
    display: flex; align-items: center; gap: 8px;
    height: 24px; font-size: 12.5px; color: var(--ink);
  }
  .contact-list svg { width: 13px; height: 13px; flex: none; }

  .job-title {
    position: absolute; left: 0; right: 0; top: 450px; text-align: center;
    font-family: "Raleway", sans-serif; font-size: 12px; color: var(--ink);
  }

  .slogan {
    position: absolute; left: 0; right: 0; top: 360px; text-align: center;
    font-family: "Raleway", sans-serif; font-size: 14px; letter-spacing: 1.4px;
    color: var(--brand-lavender);
  }
</style>
</head>
<body>

<section class="card card-front" aria-label="Business card front">
  <div class="card-frame"></div>

  <div class="brand-mark"><span class="dot"></span>R7M Meridian</div>

  <h1 class="holder-name">Dorian Valcourt</h1>
  <p class="holder-role">Owner</p>

  <ul class="contact-list">
    <li>
      <svg viewBox="0 0 16 16" aria-hidden="true"><path fill="#36479e" d="M3.5 1.5l2.3 0 1.2 3-1.5 1.2c.8 1.8 2.2 3.2 4 4l1.2-1.5 3 1.2v2.3c0 .9-.8 1.7-1.7 1.6C6.6 12.9 3.1 9.4 1.9 3.2 1.8 2.3 2.6 1.5 3.5 1.5z"/></svg>
      +64 (0) 22 4871 659
    </li>
    <li>
      <svg viewBox="0 0 16 16" aria-hidden="true"><path fill="#36479e" d="M1 6l7-4 7 4v8H1z"/><path fill="none" d="M3 6.5l5 3 5-3" stroke="#fff" stroke-width="1.2"/></svg>
      dorianv@r7mmeridian.nz
    </li>
    <li>
      <svg viewBox="0 0 16 16" aria-hidden="true"><g fill="none" stroke="#36479e" stroke-width="1.3"><circle cx="8" cy="8" r="6.3"/><ellipse cx="8" cy="8" rx="2.8" ry="6.3"/><path d="M1.7 8h12.6M2.8 4.8h10.4M2.8 11.2h10.4"/></g></svg>
      www.r7mmeridian.nz
    </li>
  </ul>

  <p class="job-title">Business Development Manager</p>
</section>

<section class="card card-back" aria-label="Business card back">
  <div class="card-frame"></div>
  <div class="brand-mark"><span class="dot"></span>R7M Meridian</div>
  <p class="slogan">"The BEST of both worlds"</p>
</section>

</body>
</html>
```